Hair Extension Packaging

Update 2/16 - please keep submissions coming, I have no front runners yet. Thanks.

I need some new packaging designed for hair extensions. I have enclose pictures of what other companies packaging looks like and a few pictures of some inspiration. I am looking for a packaging that will appeal to a 20's-30's year old demographic and I like things along the lines of glamor/lace/vintage/boudoir/damask inspired. I am going to leave colors up to your creativity for the sample artwork and ask for changes if needed. Id like the design to be a standout but not loud.

The working name for this hair is "Velvetta"
Additional Text that I would like on the packaging "100% Premium Virgin Remy Human Hair"

Please keep in mind that the background of the packaging will have many different colors laying over it so be mindful of what the color you chose can effect the hair color in the packaging - no red or orange which can make the hair appear very warm and clash with ashy colors.

Working dimensions for the sample are 22" long, 3" wide.

****Once I decide on the front of the packaging I will also need the back designed which will consist of similar design as the front but with hair care instructions printed on it.***** This finished product must include front and back artwork, open Photoshop files, and additional bleed room for printing. I don't want to waste anyone's time so once I get a front design I like I will work with that artist to create the back.

Please message me with any questions.
Updates

Project Deadline Extended
Reason: Finalizing final choices. Thanks for your submissions!

Target Market(s)

Women in there 20"s - 30's. High fashion, luxurious, glamour

Industry/Entity Type

Hair

Font styles to use
Serif
Script

Requirements
Must have
• Id love the product name to be in script and then mixed with regular font (see the makeup logo example I enclosed)
Should not have
• Should not be masculine. Forget the blue and green colors

```html
<!DOCTYPE html>
<html lang="en">
<head>
<meta charset="utf-8">
<title>Velvetta Hair Extension Packaging</title>
<link href="https://fonts.googleapis.com/css2?family=Allura&family=Lato:wght@400;700&display=swap" rel="stylesheet">
<style>
  :root {
    --page: #eeebe8;
    --paper: #ffffff;
    --ink: #8b969c;
    --badge: #111111;
    --badge-ring: #ffffff;
    --slate: #7f959e;
    --slate-light: #c8d5db;
    --slate-logo: #e9eef0;
    --slate-tint: #e9eff2;
    --taupe: #ae9f92;
    --taupe-light: #eadcca;
    --taupe-logo: #f6ece0;
    --taupe-frame: #cfc1b3;
    --taupe-tint: #f3ede7;
    --label-cream: #efe3d2;
  }
  * { box-sizing: border-box; margin: 0; padding: 0; }
  html, body { width: 1200px; height: 2951px; overflow: hidden; background: var(--page); }
  .canvas { position: relative; width: 1200px; height: 2951px; }

  .package {
    position: absolute; top: 152px; width: 389px; height: 2647px;
    overflow: hidden; box-shadow: 0 6px 18px rgba(0,0,0,0.12);
  }
  .package--slate { left: 180px; --band: var(--slate); --band-light: var(--slate-light); --logo: var(--slate-logo); --frame: var(--slate-light); --pattern: var(--slate-tint); }
  .package--taupe { left: 637px; --band: var(--taupe); --band-light: var(--taupe-light); --logo: var(--taupe-logo); --frame: var(--taupe-frame); --pattern: var(--taupe-tint); }

  .pattern-field {
    position: absolute; inset: 0;
    background: linear-gradient(180deg, var(--pattern) 0%, var(--paper) 35%, var(--pattern) 60%, var(--paper) 80%, var(--pattern) 100%);
  }
  .bands { position: absolute; inset: 0; width: 389px; height: 2647px; }

  .brand-name {
    position: absolute; top: 62px; left: 0; width: 100%;
    text-align: center; font-family: "Allura", cursive;
    font-size: 112px; line-height: 1; color: var(--logo);
    white-space: nowrap;
  }

  .badge {
    position: absolute; left: 27px; top: 270px; width: 182px; height: 182px;
    border-radius: 50%; background: var(--badge);
    border: 5px solid var(--badge-ring);
    display: flex; flex-direction: column; align-items: center; justify-content: center;
    font-family: "Lato", sans-serif; color: #fff; text-align: center;
    font-size: 18px; line-height: 1.2;
  }
  .badge strong { font-size: 22px; font-weight: 700; }

  .info-panel {
    position: absolute; left: 74px; top: 917px; width: 214px; height: 627px;
    border: 10px solid var(--frame); background: var(--paper);
  }
  .info-panel::after {
    content: ""; position: absolute; inset: 8px; border: 2px solid var(--frame);
  }
  .info-text {
    position: absolute; left: 50%; top: 50%; width: 575px; height: 150px;
    transform: translate(-50%, -50%) rotate(-90deg);
    font-family: "Lato", sans-serif; font-size: 13.5px; line-height: 34px;
    color: var(--ink); text-align: justify;
    display: flex; align-items: center;
  }

  .quality-mark {
    position: absolute; right: 60px; bottom: 18px; width: 160px; text-align: center;
  }
  .quality-mark__label {
    display: block; background: var(--label-cream); color: #6f6760;
    font-family: "Lato", sans-serif; font-weight: 700; font-size: 17px;
    letter-spacing: 0.5px; padding: 3px 0; line-height: 1.1;
  }
  .quality-mark__word {
    display: block; font-family: "Allura", cursive; color: var(--label-cream);
    font-size: 80px; line-height: 0.8; margin-top: 2px;
  }
</style>
</head>
<body>
<div class="canvas">

  <section class="package package--slate">
    <div class="pattern-field" role="img" aria-label="Faint repeating script brand-name pattern across the packaging"></div>
    <svg class="bands" viewBox="0 0 389 2647" aria-hidden="true">
      <polygon points="0,0 389,0 389,385 0,458" fill="var(--band-light)"/>
      <polygon points="0,0 389,0 389,369 0,442" fill="var(--band)"/>
      <polygon points="0,2357 389,2246 389,2647 0,2647" fill="var(--band)"/>
    </svg>
    <div class="brand-name">Velvetta</div>
    <div class="badge"><strong>100%</strong>Premium<br>Virgin Remy<br>Human Hair</div>
    <div class="info-panel">
      <p class="info-text">Lumina Clip In Hair Extensions use only the finest quality Remy Human Hair, which means that the hair has been carefully sorted after collecting from the hair donor to ensure all the cuticles are of the same length. It is by far the best quality of Clip In Human Hair Extensions on the market because of the care that is required and the time it takes to sort the hair so meticulously.</p>
    </div>
    <div class="quality-mark">
      <span class="quality-mark__label">HIGH QUALITY</span>
      <span class="quality-mark__word">hair</span>
    </div>
  </section>

  <section class="package package--taupe">
    <div class="pattern-field" role="img" aria-label="Faint repeating script brand-name pattern across the packaging"></div>
    <svg class="bands" viewBox="0 0 389 2647" aria-hidden="true">
      <polygon points="0,0 389,0 389,385 0,458" fill="var(--band-light)"/>
      <polygon points="0,0 389,0 389,369 0,442" fill="var(--band)"/>
      <polygon points="0,2357 389,2246 389,2647 0,2647" fill="var(--band)"/>
    </svg>
    <div class="brand-name">Velvetta</div>
    <div class="badge"><strong>100%</strong>Premium<br>Virgin Remy<br>Human Hair</div>
    <div class="info-panel">
      <p class="info-text">Lumina Clip In Hair Extensions use only the finest quality Remy Human Hair, which means that the hair has been carefully sorted after collecting from the hair donor to ensure all the cuticles are of the same length. It is by far the best quality of Clip In Human Hair Extensions on the market because of the care that is required and the time it takes to sort the hair so meticulously.</p>
    </div>
    <div class="quality-mark">
      <span class="quality-mark__label">HIGH QUALITY</span>
      <span class="quality-mark__word">hair</span>
    </div>
  </section>

</div>
</body>
</html>
```